Business Card Design Project

I am looking for a minimal matte background/shiny (spot UV) ink monochromatic design with a splash of neon color.

the card should be 2 sided, logo only on one side - all info and possibly logo on the other.

My creative director described the colors he imagined for the design to be:
'it's a dark field, like charcoal or a really dark burgundy, or deep blue, shot through with a neon—but just a tiny bit of it. so a charcoal field with a laser-thin streak of electric lime, safety orange, or cobalt blue. really beautiful stuff.'

here are some samples of the types of cards I am trying to create:
http://www.pictavault.example/photos/dawnpress/6967376935/in/photostream -> Vandrelle Lustre

http://www.pictavault.example/photos/dawnpress/6497659409/in/photostream -> Standard Coated (14pt/matte) with SPOT UV

http://www.pictavault.example/photos/dawnpress/6497658995/in/photostream/ -> Heavy Corvane with Raised Ink

http://www.pictavault.example/photos/dawnpress/6275629165/in/photostream/ -> Standard Coated (14pt/matte) with SPOT UV

Here is my logo:
https://www.filecrate.example/s/sigym192mlh58ge/quillorb%20logotype%20final.ai

Here are the details for info:
Dorian Elwood Marsh
email - dorian@quillorb.example
mobile - 555 013 2867
web -
quillorb.example: inventive technology applications
quillorb-tv.example: innovative video advertising

please let me know if there is anything at all that you need.

Target Market(s)

mid to large agencies that require interactive design and entrepreneurial/startup individuals/companies that need application development.

Industry/Entity Type

Safety

Requirements
Must have
• logo only on one side

```html
<!DOCTYPE html>
<html lang="en">
<head>
<meta charset="utf-8">
<title>Quillorb Business Card</title>
<link href="https://fonts.googleapis.com/css2?family=Oswald:wght@500;700&family=Arimo:wght@400;700&display=swap" rel="stylesheet">
<style>
  :root {
    --page: #ffffff;
    --charcoal: #404040;
    --ink: #231f20;
    --lime: #d4e021;
    --shadow: rgba(0, 0, 0, 0.38);
  }
  * { margin: 0; padding: 0; box-sizing: border-box; }
  html, body {
    width: 1200px;
    height: 1000px;
    overflow: hidden;
    background: var(--page);
  }
  .canvas {
    position: relative;
    width: 1200px;
    height: 1000px;
  }
  .card {
    position: absolute;
    width: 508px;
    height: 310px;
    background: var(--charcoal);
    box-shadow: 4px 4px 4px var(--shadow);
    overflow: hidden;
  }
  .card--front { left: 222px; top: 162px; }
  .card--back  { left: 427px; top: 522px; }

  .streak {
    position: absolute;
    background: var(--lime);
  }
  .streak--horizontal { left: 0; right: 0; top: 60px; height: 1px; }
  .streak--vertical { top: 0; bottom: 0; left: 68px; width: 1px; }

  .wordmark {
    position: absolute;
    left: 19px;
    top: 212px;
    font-family: "Oswald", sans-serif;
    font-weight: 500;
    font-size: 78px;
    line-height: 1;
    letter-spacing: 17px;
    color: var(--ink);
    text-transform: uppercase;
  }
  .wordmark-dot {
    position: absolute;
    left: 448px;
    top: 190px;
    width: 18px;
    height: 18px;
    background: var(--lime);
  }

  .contact {
    position: absolute;
    right: 29px;
    top: 203px;
    text-align: right;
    color: var(--ink);
  }
  .contact-name {
    font-family: "Oswald", sans-serif;
    font-weight: 700;
    font-size: 17px;
    line-height: 22px;
    letter-spacing: 3.6px;
    text-transform: uppercase;
    margin-right: -3px;
  }
  .contact-list {
    list-style: none;
    font-family: "Arimo", sans-serif;
    font-size: 12px;
    line-height: 15px;
    letter-spacing: 0.3px;
  }
  .contact-label { font-weight: 700; }
</style>
</head>
<body>
  <main class="canvas">
    <section class="card card--front" aria-label="Card front">
      <div class="streak streak--horizontal"></div>
      <div class="wordmark">Quillorb</div>
      <div class="wordmark-dot" aria-hidden="true"></div>
    </section>

    <section class="card card--back" aria-label="Card back">
      <div class="streak streak--vertical"></div>
      <div class="contact">
        <h1 class="contact-name">Dorian Elwood Marsh</h1>
        <ul class="contact-list">
          <li><span class="contact-label">email -</span> dorian@quillorb.example</li>
          <li><span class="contact-label">mobile -</span> 555 013 2867</li>
          <li><span class="contact-label">web -</span> quillorb.example: inventive technology applications</li>
          <li>quillorb-tv.example: innovative video advertising</li>
        </ul>
      </div>
    </section>
  </main>
</body>
</html>
```